Sportswear for local soccer teams Ad

Looking for a banner ad to be placed in a local soccer associations website. Pennsholdry Logo must be shown. It should be short, eyecatching and want teams to visit or contact us about their kits or training apparel. Pennsholdry is a doric word for delighted so any play on happiness, delight is fine. Size allowable is : 605x80. Also looking for a Skyscraper to be placed on all subsequent pages on their site. Size : 240x900

Target Market(s)

Football Teams

Industry/Entity Type

Sports Bar

```html
<!DOCTYPE html>
<html lang="en">
<head>
<meta charset="utf-8">
<title>Pennsholdry Banner Set</title>
<link rel="stylesheet" href="https://fonts.googleapis.com/css2?family=Oswald:wght@400;500;700&family=Roboto+Condensed:wght@700&display=swap">
<style>
  :root {
    --page-bg: #ececec;
    --banner-dark: #0c1c26;
    --banner-mid: #173545;
    --accent-blue: #1b9fd6;
    --headline-blue: #1266c9;
    --headline-green: #9aab1a;
    --white: #ffffff;
    --button-light: #f4f4f4;
    --button-shade: #bfc3c6;
    --button-text: #1a2a33;
    --photo-lime: #b8dc2a;
    --photo-grey: #5a5f62;
    --strip-grey: #c9ccce;
  }
  * { margin: 0; padding: 0; box-sizing: border-box; }
  html, body { width: 1188px; height: 1200px; overflow: hidden; }
  body {
    position: relative;
    background: var(--page-bg);
    font-family: "Oswald", "Arial Narrow", sans-serif;
    color: var(--white);
  }

  /* Presentation heading */
  .set-title {
    position: absolute;
    left: 388px;
    top: 24px;
    font-weight: 700;
    text-transform: uppercase;
    line-height: 1;
  }
  .set-title__line { display: block; font-size: 104px; letter-spacing: 1px; margin-bottom: 14px; }
  .set-title__line--blue { color: var(--headline-blue); }
  .set-title__line--green { color: var(--headline-green); font-size: 98px; }
  .set-title__number { color: var(--headline-green); }

  /* Shared banner pieces */
  .banner {
    position: absolute;
    background: linear-gradient(180deg, var(--banner-mid) 0%, var(--banner-dark) 55%, var(--banner-mid) 100%);
    overflow: hidden;
  }
  .brand { position: absolute; text-align: center; }
  .brand__circle {
    display: block;
    margin: 0 auto;
    border: 3px solid var(--white);
    border-radius: 50%;
  }
  .brand__name { display: block; font-weight: 500; color: var(--white); letter-spacing: 1px; text-transform: uppercase; }
  .photo { position: absolute; }
  .shop-button {
    position: absolute;
    display: flex;
    align-items: center;
    justify-content: center;
    gap: 8px;
    background: linear-gradient(180deg, var(--button-light) 0%, var(--button-shade) 100%);
    color: var(--button-text);
    font-family: "Roboto Condensed", "Arial Narrow", sans-serif;
    font-weight: 700;
    text-transform: uppercase;
    box-shadow: 0 2px 4px rgba(0,0,0,.5);
  }
  .web-address { position: absolute; font-weight: 500; text-transform: uppercase; color: var(--white); }

  /* Skyscraper 240x900 */
  .skyscraper { left: 50px; top: 16px; width: 300px; height: 1136px; }
  .skyscraper .brand { left: 0; top: 22px; width: 300px; }
  .skyscraper .brand__circle { width: 66px; height: 66px; }
  .skyscraper .brand__name { font-size: 30px; margin-top: 10px; }
  .skyscraper__strip {
    position: absolute; left: 0; top: 168px; width: 300px; height: 470px;
    background: var(--strip-grey);
    clip-path: polygon(0 38px, 100% 0, 100% 440px, 0 470px);
  }
  .skyscraper .photo {
    left: 0; top: 168px; width: 300px; height: 470px;
    background: linear-gradient(160deg, var(--photo-grey) 0%, var(--photo-lime) 35%, #9cc51e 60%, var(--photo-grey) 100%);
    clip-path: polygon(0 52px, 100% 14px, 100% 426px, 0 456px);
  }
  .skyscraper__offer { position: absolute; left: 0; width: 300px; text-align: center; text-transform: uppercase; font-weight: 700; line-height: 1; }
  .skyscraper__fantastic { top: 680px; font-size: 58px; }
  .skyscraper__deals { top: 736px; font-size: 112px; letter-spacing: -1px; }
  .skyscraper__types { top: 850px; font-size: 36px; font-weight: 500; color: var(--accent-blue); }
  .skyscraper__goods { top: 894px; font-size: 21px; font-weight: 500; }
  .skyscraper .shop-button { left: 56px; top: 976px; width: 190px; height: 48px; font-size: 21px; }
  .skyscraper .web-address { left: 0; width: 300px; text-align: center; top: 1070px; font-size: 23px; }

  /* Leaderboard 605x80 */
  .leaderboard { left: 388px; top: 1054px; width: 756px; height: 100px; }
  .leaderboard .photo {
    left: 0; top: 0; width: 176px; height: 100px;
    background: linear-gradient(150deg, var(--photo-grey) 0%, var(--photo-lime) 45%, var(--photo-grey) 100%);
    clip-path: polygon(0 0, 100% 0, 88% 100%, 0 100%);
  }
  .leaderboard .brand { left: 162px; top: 12px; width: 104px; }
  .leaderboard .brand__circle { width: 38px; height: 38px; border-width: 2px; }
  .leaderboard .brand__name { font-size: 15px; margin-top: 6px; }
  .leaderboard__offer { position: absolute; left: 298px; text-transform: uppercase; line-height: 1; white-space: nowrap; }
  .leaderboard__headline { top: 22px; font-size: 27px; font-weight: 500; }
  .leaderboard__sub { top: 56px; font-size: 17px; color: var(--accent-blue); font-weight: 500; }
  .leaderboard .shop-button { left: 622px; top: 22px; width: 112px; height: 28px; font-size: 13px; gap: 5px; }
  .leaderboard .web-address { left: 606px; top: 64px; font-size: 13px; }
</style>
</head>
<body>

<h1 class="set-title">
  <span class="set-title__line set-title__line--blue">Design <span class="set-title__number">#1</span></span>
  <span class="set-title__line set-title__line--green">Mock up size for</span>
  <span class="set-title__line set-title__line--blue">240x900, 605x80</span>
</h1>

<section class="banner skyscraper" aria-label="Skyscraper banner 240 by 900">
  <div class="brand">
    <span class="brand__circle"></span>
    <span class="brand__name">Pennsholdry</span>
  </div>
  <div class="skyscraper__strip"></div>
  <div class="photo" role="img" aria-label="Photo of lime green running shoes with dark stripes on a road"></div>
  <p class="skyscraper__offer skyscraper__fantastic">Fantastic</p>
  <p class="skyscraper__offer skyscraper__deals">Deals</p>
  <p class="skyscraper__offer skyscraper__types">On all types of</p>
  <p class="skyscraper__offer skyscraper__goods">Clothing and footwear</p>
  <a class="shop-button">Shop now
    <svg width="26" height="22" viewBox="0 0 26 22" aria-hidden="true"><path d="M1 2h4l3 12h13l3-9H7" fill="none" stroke="#1a2a33" stroke-width="2.2" stroke-linejoin="round"/><circle cx="10" cy="18.5" r="2" fill="#1a2a33"/><circle cx="19" cy="18.5" r="2" fill="#1a2a33"/></svg>
  </a>
  <p class="web-address">www.pennsholdry.com</p>
</section>

<section class="banner leaderboard" aria-label="Leaderboard banner 605 by 80">
  <div class="photo" role="img" aria-label="Photo of lime green running shoes on a road"></div>
  <div class="brand">
    <span class="brand__circle"></span>
    <span class="brand__name">Pennsholdry</span>
  </div>
  <p class="leaderboard__offer leaderboard__headline">Fantastic deals on all</p>
  <p class="leaderboard__offer leaderboard__sub">Types of clothing and footwear</p>
  <a class="shop-button">Shop now
    <svg width="16" height="14" viewBox="0 0 26 22" aria-hidden="true"><path d="M1 2h4l3 12h13l3-9H7" fill="none" stroke="#1a2a33" stroke-width="2.4" stroke-linejoin="round"/><circle cx="10" cy="18.5" r="2" fill="#1a2a33"/><circle cx="19" cy="18.5" r="2" fill="#1a2a33"/></svg>
  </a>
  <p class="web-address">www.pennsholdry.com</p>
</section>

</body>
</html>
```